Flyer Design For Building & Decorating Company

We need an A6 double-sided colour flyer for a letter-box marketing campaign. We are a building and decorating company based in West London. We saw a flyer that we liked and have attached it as an example of the sort of thing we're looking for (see attached files Example A6 Flyer - Front.png and Example A6 Flyer - Back.png). Please note that we're not expecting the designer to slavishly follow this design, more to use it as a jumping-off point.

The design must incorporate a strong call to action, e.g., Call Us For A Free, No-Obligation Quote.

The textual information that must be included in the flyer (contact methods, tagline, services, etc.) are included in the attached file Flyer Text.docx.

Also included as attachments are a selection of images used on our website (files bathroom.png, carpentry.png, decorating.jpg,
flooring.jpg, painting_decorating.jpg, repointing.jpg and work_ on_scaffold.jpg). Please include these images on the flyer (at least one image on each side), or use stock images if any of these are unsuitable.

The company logo will also need to be included in the flyer - see attached file logo.png

The images on our website have all had to be re-sized from the originals. I've attached a number of the original images to this brief, as these are the highest resolution versions of the images that we have. I would ask that you use the versions attached to the brief, but if you feel that other images from our website would work better on your flyer design, please let me know and I'll attach them to this brief.

Finally, we've attached guideline notes from our printer (see attached file Printer's Requirements.docx) - please ensure these are adhered to where relevant.

Target Market(s)

People in West London who require building or decorating work to be done on their properties.

Industry/Entity Type

Marketing

Requirements
Must have
• A6 double-sided colour flyer using the text we provided and some of the images provided.

The call to action must be prominent and eye-catching, as the only purpose of the flyer is to get recipients to contact our company for a quote.

```html
<!DOCTYPE html>
<html lang="en">
<head>
<meta charset="utf-8">
<title>West London Builders &amp; Decorators – Flyer</title>
<link rel="stylesheet" href="https://fonts.googleapis.com/css2?family=Oswald:wght@400;500;600;700&family=Roboto+Condensed:wght@400;700&display=swap">
<style>
  :root{
    --brown:#5b2a0f;
    --brown-deep:#3f1b08;
    --orange:#f08a10;
    --orange-soft:#f6a534;
    --cream:#f7efcf;
    --cream-deep:#efe2b4;
    --white:#ffffff;
  }
  *{margin:0;padding:0;box-sizing:border-box}
  html,body{width:851px;height:1200px;overflow:hidden;background:var(--cream)}
  .flyer{position:relative;width:851px;height:1200px;background:var(--cream);font-family:"Oswald",sans-serif;overflow:hidden}

  .logo-block{position:absolute;left:88px;top:0;width:190px;height:215px;background:var(--brown);display:flex;flex-direction:column;align-items:center;justify-content:center;gap:14px;z-index:3}
  .logo-block .mark{width:46px;height:46px;background:var(--cream)}
  .logo-block .name{color:var(--cream);font-family:"Oswald",sans-serif;font-weight:500;font-size:22px;text-align:center;line-height:1.15;letter-spacing:1px}

  .call-bar{position:absolute;left:300px;top:0;width:551px;height:130px;background:var(--brown);display:flex;align-items:center;padding-left:22px;z-index:2}
  .call-label{color:var(--orange);font-weight:700;font-size:44px;line-height:.98;text-transform:uppercase;margin-right:26px}
  .call-numbers{border-left:3px solid var(--orange);padding-left:18px;color:var(--orange);font-weight:600;font-size:38px;line-height:1.2}

  .hero-photo{position:absolute;left:0;top:130px;width:851px;height:560px;background:linear-gradient(135deg,#f1f1f0 0%,#d9d9db 45%,#a9a39b 75%,#6c5b4a 100%);z-index:1}

  .headline{position:absolute;left:278px;top:612px;width:573px;height:180px;background:linear-gradient(180deg,#6a3414,var(--brown-deep));padding:18px 0 0 26px;z-index:2}
  .headline h1{color:var(--cream);font-weight:600;font-size:50px;line-height:1.02}
  .headline p{color:var(--cream);font-family:"Roboto Condensed",sans-serif;font-weight:700;font-size:24px;margin-top:10px}

  .services-tab{position:absolute;left:40px;top:680px;width:185px;height:50px;background:var(--orange);color:var(--white);font-weight:600;font-size:34px;line-height:50px;text-align:center;z-index:3}

  .services{position:absolute;top:740px;list-style:none;color:var(--orange);font-family:"Roboto Condensed",sans-serif;font-weight:700;font-size:33px;line-height:1.12}
  .services li{position:relative;padding-left:34px;margin-bottom:20px;white-space:nowrap}
  .services li svg{position:absolute;left:0;top:8px;width:26px;height:26px}
  .services.col-a{left:18px;width:200px}
  .services.col-b{left:226px;top:815px;width:300px}

  .detail-photo{position:absolute;left:556px;top:826px;width:295px;height:254px;background:linear-gradient(160deg,#e6c79a,#b98551 60%,#6b4a2e)}

  .footer{position:absolute;left:0;top:1120px;width:851px;height:80px;border-top:3px solid var(--orange);background:var(--cream-deep);display:flex;align-items:center;padding:0 50px;font-family:"Roboto Condensed",sans-serif;color:var(--brown);font-size:20px;line-height:1.25}
  .footer .address{display:flex;align-items:center;gap:10px;width:420px}
  .footer .online{display:flex;flex-direction:column}
  .footer .online b{color:var(--orange);margin-right:10px}
  .pin{width:18px;height:22px;flex:none}
</style>
</head>
<body>
<main class="flyer">
  <div class="logo-block">
    <span class="mark"></span>
    <span class="name">HARWELL<br>RENOVATIONS</span>
  </div>

  <div class="call-bar">
    <div class="call-label">Call<br>Now</div>
    <div class="call-numbers">T : 0208 555 0142<br>M : 07700 900318</div>
  </div>

  <div class="hero-photo" role="img" aria-label="Photo of a plumber fitting pipes under a kitchen sink while a homeowner looks on"></div>

  <div class="headline">
    <h1>West London<br>Builders &amp; Decorators</h1>
    <p>Quality Renovations At Affordable Prices</p>
  </div>

  <div class="services-tab">SERVICES</div>

  <ul class="services col-a">
    <li><svg viewBox="0 0 28 28"><polyline points="3,15 11,23 25,4" fill="none" stroke="#f08a10" stroke-width="5" stroke-linecap="round" stroke-linejoin="round"/></svg>Bathrooms<br>Kitchens</li>
    <li><svg viewBox="0 0 28 28"><polyline points="3,15 11,23 25,4" fill="none" stroke="#f08a10" stroke-width="5" stroke-linecap="round" stroke-linejoin="round"/></svg>Tiling</li>
    <li><svg viewBox="0 0 28 28"><polyline points="3,15 11,23 25,4" fill="none" stroke="#f08a10" stroke-width="5" stroke-linecap="round" stroke-linejoin="round"/></svg>Painting<br>Decorating</li>
    <li><svg viewBox="0 0 28 28"><polyline points="3,15 11,23 25,4" fill="none" stroke="#f08a10" stroke-width="5" stroke-linecap="round" stroke-linejoin="round"/></svg>Plastering</li>
    <li><svg viewBox="0 0 28 28"><polyline points="3,15 11,23 25,4" fill="none" stroke="#f08a10" stroke-width="5" stroke-linecap="round" stroke-linejoin="round"/></svg>Carpentry</li>
  </ul>

  <ul class="services col-b">
    <li><svg viewBox="0 0 28 28"><polyline points="3,15 11,23 25,4" fill="none" stroke="#f08a10" stroke-width="5" stroke-linecap="round" stroke-linejoin="round"/></svg>Flooring</li>
    <li><svg viewBox="0 0 28 28"><polyline points="3,15 11,23 25,4" fill="none" stroke="#f08a10" stroke-width="5" stroke-linecap="round" stroke-linejoin="round"/></svg>Plumbing</li>
    <li><svg viewBox="0 0 28 28"><polyline points="3,15 11,23 25,4" fill="none" stroke="#f08a10" stroke-width="5" stroke-linecap="round" stroke-linejoin="round"/></svg>Electrical Works</li>
    <li><svg viewBox="0 0 28 28"><polyline points="3,15 11,23 25,4" fill="none" stroke="#f08a10" stroke-width="5" stroke-linecap="round" stroke-linejoin="round"/></svg>Brickwork</li>
    <li><svg viewBox="0 0 28 28"><polyline points="3,15 11,23 25,4" fill="none" stroke="#f08a10" stroke-width="5" stroke-linecap="round" stroke-linejoin="round"/></svg>General Repairs</li>
  </ul>

  <div class="detail-photo" role="img" aria-label="Photo of carpentry tools: hammer, nails and measuring tape on wooden boards"></div>

  <footer class="footer">
    <div class="address">
      <svg class="pin" viewBox="0 0 18 22"><path d="M9 1a7 7 0 0 0-7 7c0 5 7 13 7 13s7-8 7-13a7 7 0 0 0-7-7z" fill="#f08a10"/><circle cx="9" cy="8" r="2.6" fill="#efe2b4"/></svg>
      <span>18 Linden Grove,<br>Ealing, London W5 4QT</span>
    </div>
    <div class="online">
      <span><b>E:</b>hello@harwell-renovations.co.uk</span>
      <span><b>W:</b>www.harwell-renovations.co.uk</span>
    </div>
  </footer>
</main>
</body>
</html>
```